Home page web design for a lawn specialist business

-The design must be based around the attached HPID (home page information design) called Turf Tidings HPID. I've attached Word and PDF versions - these are the same. The table boxes are just for approximate placement of information and you can use boxes and bold shapes for this design.

All fonts used in the HPID are only examples - you can use any Google font you wish.

- Text that is in orange is for your information only. Text to go on the design is black. Some instructions are in the HPID. Please be creative!

-The design needs to be modern and exciting - colours are to be the green of the logo, and white ...and then choose dark green, or dark grey or black.

Logo - attached (it's not great quality but don't worry, we'll replace it later)

- I've provided the images for the galleries - they are labelled and will match the name in the HPID. Please use the supplied images!

- Examples of some websites that have great design... don't copy them please but they are similar in look to what we are after....
www.qmbbuildworks.co.nz
http://www.rim-safeguard.co.nz/
http://www.lumenhomes.wb.gs/

Important: Width of content will be 1280 pixels when implemented as a web page but the winning design will need to supplied be on a 2000 pixel wide background so nav bars and background can extend outside the 1280 width.
Header height (without nav bar) 150-160 pixels.

We don't comment on individual designs but will choose a winning design promptly.

Industry/Entity Type

Business

Number of Pages Required

1 page

Font styles to use
Sans Serif

Requirements
Must have
• clean, modern, well-spaced design

```html
<!DOCTYPE html>
<html lang="en">
<head>
<meta charset="utf-8">
<title>Turf Tidings – Lawn Specialists</title>
<link href="https://fonts.googleapis.com/css2?family=Oswald:wght@400;500&family=Open+Sans:wght@400;600;700&display=swap" rel="stylesheet">
<style>
:root{
  --green:#2b9b3c;
  --green-dark:#1f7d2e;
  --leaf:#5fb32a;
  --lime:#8cc63f;
  --pale:#eaf4df;
  --brown:#4a2a12;
  --brown-light:#6b3f1d;
  --ink:#222;
  --grey:#555;
  --night:#151515;
  --white:#fff;
}
*{box-sizing:border-box;margin:0;padding:0}
html,body{width:1200px;height:2303px;overflow:hidden}
body{position:relative;background:var(--white);font-family:"Open Sans",Arial,sans-serif;color:var(--ink)}
.abs{position:absolute}

/* header */
.brand{left:48px;top:18px;display:flex;align-items:center;gap:16px}
.brand-dot{width:96px;height:96px;border-radius:50%;background:var(--leaf)}
.brand-name{font-weight:700;font-size:30px;color:var(--green)}
.contact-block{right:48px;top:8px;text-align:right}
.contact-block .title{font-family:"Oswald",sans-serif;font-size:27px;color:var(--green);line-height:1.2}
.contact-block .tag{font-size:13px;color:var(--grey);margin-top:2px}
.contact-block .region{font-size:15px;font-weight:600;color:var(--green);margin-top:10px}
.contact-block .phone{font-family:"Oswald",sans-serif;font-size:28px;color:var(--ink);line-height:1.15}

/* nav */
.nav{left:0;top:133px;width:1200px;height:44px;background:linear-gradient(#6a3e1b,#40230d);display:flex;justify-content:space-between;align-items:center;padding:0 51px}
.nav a{font-family:"Oswald",sans-serif;font-size:16px;color:var(--white);text-decoration:none;padding:0 18px;height:44px;line-height:44px}
.nav a.active{background:var(--green)}

/* hero */
.hero{left:0;top:177px;width:1200px;height:445px;background:linear-gradient(#d9ecf6 0%,#cfe6c0 55%,#4e9a2b 80%,#2f7a1e 100%)}
.hero-photo{left:51px;top:189px;width:1101px;height:403px;border:6px solid #f4f4f0;background:linear-gradient(100deg,#7a6a55 0%,#8c7c66 45%,#3d8f2c 52%,#5db53a 100%)}
.ba-label{top:357px;height:44px;line-height:44px;font-family:"Oswald",sans-serif;font-size:28px;color:var(--white);background:rgba(20,20,20,.85);padding:0 22px}
.ba-before{left:476px;transform:skewX(-10deg)}
.ba-after{left:612px;transform:skewX(-10deg)}
.hero-arrow{top:367px;width:40px;height:40px;background:#222;border-radius:4px;display:flex;align-items:center;justify-content:center}

/* intro */
.intro-title{left:0;top:638px;width:1200px;text-align:center;font-family:"Oswald",sans-serif;font-weight:400;font-size:32px;color:var(--leaf)}
.intro-sub{left:0;top:684px;width:1200px;text-align:center;font-size:17px;color:var(--green)}
.intro-text{left:51px;top:735px;width:1100px;text-align:center;font-size:11.5px;line-height:1.8;color:var(--ink)}

/* services band */
.band{left:0;top:829px;width:1200px;height:679px;background:linear-gradient(var(--pale),#f6fbf1)}
.card{top:852px;width:525px;height:300px;background:var(--white);border:1px solid #cfe2c0}
.card-head{position:absolute;left:-1px;top:41px;width:525px;height:62px;background:var(--green)}
.card-head h2{position:absolute;left:116px;top:8px;font-family:"Oswald",sans-serif;font-weight:400;font-size:31px;color:var(--white)}
.card-icon{position:absolute;left:18px;top:0;width:92px;height:92px;border-radius:50%;background:var(--white);border:5px solid var(--green)}
.card-img{position:absolute;left:22px;top:124px;width:232px;height:148px;border:4px solid #eee}
.card-text{position:absolute;left:278px;top:124px;width:222px;font-size:12.5px;line-height:1.6}
.btn{display:inline-block;background:var(--brown);color:var(--white);font-family:"Oswald",sans-serif;font-size:14px;padding:0 14px;height:34px;line-height:34px;text-transform:uppercase}
.card .btn{position:absolute;left:278px;top:244px}

.section-title{font-family:"Oswald",sans-serif;font-weight:400;font-size:22px;color:var(--green);top:1188px}
.section-rule{top:1226px;width:525px;height:2px;background:#cfe2c0}
.faq-box{left:51px;top:1237px;width:525px;height:230px;border:5px solid var(--white);box-shadow:0 2px 6px rgba(0,0,0,.15);background:linear-gradient(#e1e7da,#9bc97a 55%,#3f9c2e)}
.faq-overlay{position:absolute;left:40px;top:95px;width:430px;color:var(--white);font-size:13px;line-height:1.45;background:rgba(0,0,0,.35);padding:8px 12px}
.faq-box .btn{position:absolute;left:40px;top:146px}
.gallery-box{left:624px;top:1237px;width:525px;height:236px;background:var(--white);border:1px solid #9dd07a}
.gallery-pic{position:absolute;top:8px;width:250px;height:140px}
.gallery-pic span{position:absolute;left:0;top:0;width:100%;height:26px;line-height:26px;background:rgba(20,20,20,.85);color:var(--white);text-align:center;font-family:"Oswald",sans-serif;font-size:15px}
.gallery-caption{position:absolute;left:8px;top:148px;width:509px;height:40px;background:rgba(20,20,20,.75);color:var(--white);font-size:12px;text-align:center;line-height:1.35;padding-top:3px}
.gallery-link{position:absolute;left:8px;top:204px;font-size:13px;color:var(--green)}

/* video */
.video-lead{left:51px;top:1528px;font-size:14px;color:var(--green)}
.video{left:58px;top:1571px;width:534px;height:237px;border:5px solid #e6e6e6;background:linear-gradient(#5f7a55,#8fa07a 50%,#5d8f3c)}
.video-bar{position:absolute;left:0;bottom:0;width:100%;height:26px;background:#111;display:flex;align-items:center;gap:10px;padding:0 10px;color:var(--white);font-size:11px}
.video-track{flex:1;height:5px;background:#555;border-radius:3px}
.play{position:absolute;left:238px;top:78px;width:48px;height:48px;border-radius:50%;background:var(--white);display:flex;align-items:center;justify-content:center}
.about-block{left:686px;top:1560px;width:465px}
.about-title{font-family:"Oswald",sans-serif;font-weight:400;font-size:36px;line-height:1.3;color:var(--green);margin-bottom:12px}
.about-text{font-size:12px;line-height:1.6}
.about-text p{margin-bottom:9px}
.about-block .btn{margin-top:8px}

/* testimonials */
.testimonials{left:0;top:1843px;width:1200px;height:184px;background:linear-gradient(#7dbb3c,#4f9a2a 55%,#2f7a1e)}
.quote{top:1877px;width:341px;height:81px;background:var(--white);border-radius:6px;font-style:italic;font-size:13.5px;line-height:1.5;color:#444;padding:14px 18px}
.quote::after{content:"";position:absolute;right:40px;bottom:-14px;border:14px solid transparent;border-top-color:var(--white);border-bottom:0}
.quote-name{top:1977px;font-size:12px;color:var(--white);text-align:right;white-space:nowrap}
.quote-name b{font-weight:700}

/* footer */
.footer{left:0;top:2027px;width:1200px;height:276px;background:var(--night)}
.quick-title{left:51px;top:2040px;font-family:"Oswald",sans-serif;font-weight:400;font-size:21px;color:var(--white)}
.links{top:2082px;list-style:none;font-size:12px;color:#ddd}
.links li{height:25px}
.links li::before{content:"› ";color:var(--lime)}
.foot-brand{left:352px;top:2060px;width:150px;text-align:center}
.foot-brand .brand-dot{width:100px;height:100px;margin:0 auto 10px;background:#ccc}
.foot-brand span{font-weight:700;font-size:14px;color:var(--white)}
.quote-title{left:539px;top:2036px;font-family:"Oswald",sans-serif;font-weight:400;font-size:23px;color:var(--lime)}
.quote-sub{left:539px;top:2070px;font-size:15px;font-style:italic;color:var(--lime)}
.quote-sub b{font-family:"Oswald",sans-serif;font-style:normal;font-weight:400;font-size:22px}
.field{height:30px;background:var(--white);font-size:11px;color:#777;padding:0 8px;line-height:30px}
.call-btn{left:539px;top:2195px;width:96px;height:30px;line-height:30px;text-align:center;background:var(--lime);color:var(--night);font-family:"Oswald",sans-serif;font-size:13px}
.copyright{left:0;top:2242px;width:1200px;height:61px;background:#0b0b0b;text-align:center;color:#bbb;font-size:12px;line-height:61px}
</style>
</head>
<body>

<header>
  <div class="abs brand"><span class="brand-dot"></span><span class="brand-name">Verdant Lawn Studio</span></div>
  <div class="abs contact-block">
    <div class="title">LAWN SPECIALISTS</div>
    <div class="tag">...from ground preparation to lawn aftercare</div>
    <div class="region">SERVICING THE AUCKLAND REGION</div>
    <div class="phone">0800 42 63 19</div>
  </div>
</header>

<nav class="abs nav">
  <a class="active">Home</a><a>About us</a><a>Services</a><a>Lawn care</a><a>Seasonal care</a><a>Hydroseeding</a><a>FAQs</a><a>Before &amp; After Gallery</a><a>Quote / Contact</a>
</nav>

<section>
  <div class="abs hero" role="img" aria-label="Lush lawn and sky backdrop"></div>
  <div class="abs hero-photo" role="img" aria-label="Courtyard before and after new lawn: bare soil on the left, green grass on the right"></div>
  <div class="abs ba-label ba-before">BEFORE</div>
  <div class="abs ba-label ba-after">AFTER</div>
  <div class="abs hero-arrow" style="left:51px"><svg width="14" height="20"><path d="M11 2 3 10l8 8" stroke="#fff" stroke-width="3" fill="none"/></svg></div>
  <div class="abs hero-arrow" style="left:1112px"><svg width="14" height="20"><path d="m3 2 8 8-8 8" stroke="#fff" stroke-width="3" fill="none"/></svg></div>
</section>

<section>
  <h1 class="abs intro-title">You can always spot a Turf Tidings lawn</h1>
  <p class="abs intro-sub">It's the one that turns your neighbours green with envy.</p>
  <p class="abs intro-text">If you want a lawn or playing field that looks good throughout the year, talk to us. Turf Tidings are New Zealand's experts in high quality grass seeding and lawn maintenance, creating the lushest lawns you'll ever see. With high-tech equipment, years of experience and expert aftercare, nobody knows grass like Turf Tidings. There are many factors that influence the quality of a lawn, including seasonality, growing conditions, shade, seed types, and time. A one-size-fits-all solution couldn't possibly guarantee a great lawn, so we provide personalised advice, a full range of seeding techniques.</p>
</section>

<section>
  <div class="abs band"></div>

  <article class="abs card" style="left:51px">
    <div class="card-head"><h2>Grass Seeding Services</h2></div>
    <div class="card-icon"></div>
    <div class="card-img" role="img" aria-label="Freshly hydroseeded garden bed" style="background:linear-gradient(#6f8f6a,#3f9a8c)"></div>
    <p class="card-text">With a wide range of grass seed applications to choose from, including hydroseeding and instant lawn, there is an option to suit your property and your requirements.</p>
    <span class="btn">More about grass seeding</span>
  </article>

  <article class="abs card" style="left:624px">
    <div class="card-head"><h2>Lawn care maintenance</h2></div>
    <div class="card-icon"></div>
    <div class="card-img" role="img" aria-label="Sprinkler watering a green lawn" style="background:linear-gradient(#9fd46a,#3f9a2a)"></div>
    <p class="card-text">As well as lawn care services, the team at Turf Tidings provides helpful information for regular upkeep of your residential or commercial lawn.</p>
    <span class="btn">More about ongoing lawn care</span>
  </article>

  <h3 class="abs section-title" style="left:51px">FAQs about grass seeding and lawn care</h3>
  <div class="abs section-rule" style="left:51px"></div>
  <h3 class="abs section-title" style="left:624px">Before and after lawn photos</h3>
  <div class="abs section-rule" style="left:624px"></div>

  <div class="abs faq-box" role="img" aria-label="Backyard lawn with trees">
    <p class="faq-overlay">For more information, read our frequently asked questions regarding grass seeding and lawn care.</p>
    <span class="btn">Grass seeding &amp; lawn care FAQs</span>
  </div>

  <div class="abs gallery-box">
    <div class="gallery-pic" role="img" aria-label="Bare section before seeding" style="left:8px;background:linear-gradient(#b8c4cc,#6d6253)"><span>BEFORE</span></div>
    <div class="gallery-pic" role="img" aria-label="Same section with new lawn" style="left:267px;background:linear-gradient(#b8c4cc,#4ea52e)"><span>AFTER</span></div>
    <p class="gallery-caption">See what you potential new lawn could look like by viewing a range of before and<br>after lawn seeding photos.</p>
    <a class="gallery-link">BEFORE AND AFTER PHOTOS &gt;</a>
  </div>
</section>

<section>
  <p class="abs video-lead">Watch the video on how Turf Tidings can transform your empty spaces into beautiful green grass lawns</p>
  <div class="abs video" role="img" aria-label="Video still of a finished garden lawn">
    <div class="play"><svg width="18" height="20"><path d="M3 1v18l14-9z" fill="#222"/></svg></div>
    <div class="video-bar"><svg width="10" height="12"><path d="M0 0v12l10-6z" fill="#fff"/></svg><span>04:59</span><div class="video-track"></div><svg width="12" height="12"><path d="M1 4V1h3M8 1h3v3M11 8v3H8M4 11H1V8" stroke="#fff" fill="none"/></svg></div>
  </div>
  <div class="abs about-block">
    <h2 class="about-title">Turf Tidings...</h2>
    <div class="about-text">
      <p>For all things grass, you need the best! Turf Tidings are skilled specialists when it comes to creating the perfect lawn for your property.</p>
      <p>From pre-seeding preparation to a full range of grass seeding services and lawn after care options, you'll enjoy a healthy green lawn for many years.</p>
      <p>Selling your property? Turf Tidings will add the wow factor to the outdoor areas of your home with a lush green lawn.</p>
    </div>
    <span class="btn">Find out more</span>
  </div>
</section>

<section>
  <div class="abs testimonials" role="img" aria-label="Close-up of grass blades"></div>
  <blockquote class="abs quote" style="left:51px">I would recommend Turf Tidings to anyone who wants an amazing lawn</blockquote>
  <blockquote class="abs quote" style="left:438px">I would recommend Turf Tidings to anyone who wants an amazing lawn</blockquote>
  <blockquote class="abs quote" style="left:806px">I would recommend Turf Tidings to anyone who wants an amazing lawn</blockquote>
  <p class="abs quote-name" style="right:808px"><b>Sam Harlow</b> - Homeowner, Glenfield</p>
  <p class="abs quote-name" style="right:421px"><b>Sam Harlow</b> - Homeowner, Glenfield</p>
  <p class="abs quote-name" style="right:53px"><b>Sam Harlow</b> - Homeowner, Glenfield</p>
</section>

<footer>
  <div class="abs footer"></div>
  <h4 class="abs quick-title">Quick Links</h4>
  <ul class="abs links" style="left:60px"><li>Home</li><li>About Us</li><li>Services</li><li>Lawn care</li><li>Seasonal care</li></ul>
  <ul class="abs links" style="left:172px"><li>Hydroseeding</li><li>FAQs</li><li>Before &amp; After Gallery</li><li>Quote / Contact</li></ul>
  <div class="abs foot-brand"><div class="brand-dot"></div><span>Verdant Lawn Studio</span></div>
  <h4 class="abs quote-title">Get a quote for your new lawn!</h4>
  <p class="abs quote-sub">Fill in the form or phone us on <b>0800 42 63 19.</b></p>
  <div class="abs field" style="left:539px;top:2107px;width:196px">First Name</div>
  <div class="abs field" style="left:744px;top:2107px;width:198px">Last Name</div>
  <div class="abs field" style="left:951px;top:2107px;width:198px">Email Address</div>
  <div class="abs field" style="left:539px;top:2146px;width:196px">Contact Phone</div>
  <div class="abs field" style="left:744px;top:2146px;width:405px">Details</div>
  <div class="abs call-btn">CALL ME BACK</div>
  <p class="abs copyright">© VERDANT LAWN STUDIO . All Rights Reserved 2015.</p>
</footer>

</body>
</html>
```